Trade Show Banner

Looking for a design for 36" x 90" stretched fabric display.
Commercial construction company, can include Chicago high rise buildings, blue prints, steel studs.
List of types of work should include:
Commercial office build-out
Hospital expansion
Educational and institutional
Laboratory and research
Dental and medical office
Veterinary Clinics

website brolmerconstruction.com

Target Market(s)

Architects and General Contractors

Industry/Entity Type

Commercial Construction

Colors
0054AA
0677BA
7BADD7
CADEEF
E8F1F8

Requirements
Must have
• Our logo, blueprints, chicago high rise
Should not have
• no cartoon construction logos, no houses

```html
<!DOCTYPE html>
<html lang="en">
<head>
<meta charset="UTF-8">
<title>Brolmer Construction – Trade Show Banner</title>
<link rel="stylesheet" href="https://fonts.googleapis.com/css2?family=Roboto:wght@400;700;900&family=Fira+Sans:wght@400&display=swap">
<style>
  :root {
    --brand-deep: #0054AA;
    --brand-blue: #0677BA;
    --brand-sky: #7BADD7;
    --brand-mist: #CADEEF;
    --brand-ice: #E8F1F8;
    --list-bar: #29B4F0;
    --ink: #1f1f1f;
    --footer-dark: #3d3d3d;
    --white: #ffffff;
  }
  * { margin: 0; padding: 0; box-sizing: border-box; }
  html, body { width: 1200px; height: 3000px; overflow: hidden; background: var(--white); }
  .banner {
    position: relative;
    width: 1200px;
    height: 3000px;
    overflow: hidden;
    background: var(--white);
    font-family: "Roboto", Arial, sans-serif;
  }

  .brand {
    position: absolute;
    top: 130px;
    left: 0;
    width: 1200px;
    display: flex;
    align-items: center;
    justify-content: center;
    gap: 26px;
  }
  .brand-square {
    width: 110px;
    height: 110px;
    background: var(--brand-deep);
  }
  .brand-name {
    font-weight: 900;
    font-size: 62px;
    line-height: 1.05;
    color: var(--brand-deep);
    letter-spacing: 1px;
    text-transform: uppercase;
  }

  .hero-photo {
    position: absolute;
    left: 0;
    top: 310px;
    width: 1089px;
    height: 1243px;
    border-radius: 0 120px 120px 0;
    background:
      radial-gradient(ellipse 45% 30% at 35% 55%, #8fa9e2 0%, rgba(143,169,226,0) 100%),
      linear-gradient(160deg, #1d3f96 0%, #2f56b4 35%, #3c66c4 60%, #1c3a86 100%);
  }
  .hero-headline {
    position: absolute;
    left: 105px;
    top: 385px;
    color: var(--white);
    font-weight: 700;
    font-size: 105px;
    line-height: 110px;
    text-transform: uppercase;
  }
  .hero-sub {
    position: absolute;
    left: 105px;
    top: 606px;
    color: var(--white);
    font-weight: 700;
    font-size: 41px;
    text-transform: uppercase;
  }

  .services {
    position: absolute;
    left: 0;
    top: 1107px;
    width: 571px;
    height: 874px;
    background: var(--brand-blue);
    border-radius: 0 82px 175px 0;
    padding: 76px 0 0 72px;
    list-style: none;
  }
  .services li {
    position: relative;
    padding-left: 47px;
    height: 131px;
    color: var(--white);
    font-size: 44px;
    line-height: 47px;
    text-transform: uppercase;
    letter-spacing: 0.5px;
  }
  .services li::before {
    content: "";
    position: absolute;
    left: 0;
    top: 5px;
    width: 8px;
    height: 76px;
    border-radius: 4px;
    background: var(--list-bar);
  }

  .specialties {
    position: absolute;
    left: 642px;
    top: 1622px;
    width: 430px;
    font-family: "Fira Sans", Arial, sans-serif;
    font-size: 38px;
    line-height: 50px;
    color: var(--ink);
  }

  .gallery-tile {
    position: absolute;
    width: 451px;
    height: 291px;
    border-radius: 18px;
  }
  .tile-steel { left: 129px; top: 2045px; background: linear-gradient(170deg, #8fc3ea 0%, #4f8fc6 60%, #2f6aa5 100%); }
  .tile-doors { left: 631px; top: 2045px; background: linear-gradient(90deg, #8a4a25 0%, #c9b8a0 50%, #8a4a25 100%); }
  .tile-plans { left: 129px; top: 2371px; background: linear-gradient(160deg, #e9e4dc 0%, #d7dde6 60%, #c8b79a 100%); }
  .tile-stairs { left: 631px; top: 2371px; background: linear-gradient(90deg, #c9b59a 0%, #9a6a3f 55%, #3b3b3b 100%); }

  .website {
    position: absolute;
    left: 0;
    top: 2740px;
    width: 1200px;
    text-align: center;
    font-weight: 700;
    font-size: 53px;
    letter-spacing: -0.5px;
    color: var(--ink);
    text-transform: uppercase;
  }

  .footer-band {
    position: absolute;
    left: 108px;
    top: 2837px;
    width: 1092px;
    height: 163px;
    background: var(--footer-dark);
    border-radius: 118px 0 0 0;
  }
</style>
</head>
<body>
  <main class="banner">
    <header class="brand">
      <div class="brand-square"></div>
      <div class="brand-name">Brolmer<br>Construction</div>
    </header>

    <div class="hero-photo" role="img" aria-label="Upward view of Chicago glass high-rise towers against a blue sky"></div>
    <h1 class="hero-headline">We can work<br>for your future</h1>
    <p class="hero-sub">Visit us today for better results</p>

    <ul class="services">
      <li>Commercial<br>office build-out</li>
      <li>Hospital<br>expansion</li>
      <li>Educational and<br>institutional</li>
      <li>Laboratory and<br>research</li>
      <li>Dental and<br>medical office</li>
      <li>Veterinary<br>clinics</li>
    </ul>

    <p class="specialties">Specialize in Metal Framing, Drywall Installation, Acoustic and Specialty Ceilings, as well as installation of Doors and Frames in commercial settings</p>

    <div class="gallery-tile tile-steel" role="img" aria-label="Steel stud framing against a bright sky"></div>
    <div class="gallery-tile tile-doors" role="img" aria-label="Wooden doors and frames in a commercial lobby"></div>
    <div class="gallery-tile tile-plans" role="img" aria-label="Hands reviewing blueprints on a table"></div>
    <div class="gallery-tile tile-stairs" role="img" aria-label="Finished interior with wood floor and metal staircase"></div>

    <p class="website">brolmerconstruction.com</p>

    <div class="footer-band"></div>
  </main>
</body>
</html>
```